Ridgeway Sparks Business cards

We require somebody to design business cards for our new business.

Target Market(s)

Mining, haulage and civil.

Industry/Entity Type

Auto electrician in mining industry

Contact Information for Business Card

ABN, business email address, mobile number.

Colors
00AB8E
00BBA5
67D7C9
C6EFE9
E9F9F6

Requirements
Must have
• Services I offer: Breakdowns, Field Service, A/C Systems, Machine rewires, mine site vehicle fit outs

```html
<!DOCTYPE html>
<html lang="en">
<head>
<meta charset="utf-8">
<title>Ridgeway Sparks Business Cards</title>
<link rel="stylesheet" href="https://fonts.googleapis.com/css2?family=Roboto:wght@400;500;700&display=swap">
<style>
  :root {
    --bg: #2a2a2a;
    --card: #000000;
    --teal: #00AB8E;
    --teal-bright: #00BBA5;
    --teal-soft: #67D7C9;
    --text: #ffffff;
    --rule: #d9d9d9;
  }
  * { box-sizing: border-box; margin: 0; padding: 0; }
  html, body {
    width: 1200px; height: 875px; overflow: hidden;
    background: var(--bg);
    font-family: "Roboto", Arial, sans-serif;
    color: var(--text);
  }
  .sheet {
    width: 1200px; height: 875px;
    display: flex; align-items: center; justify-content: center; gap: 40px;
  }
  .card {
    position: relative;
    width: 540px; height: 310px;
    background: var(--card);
    border-radius: 22px;
    box-shadow: 0 14px 40px rgba(0,0,0,.55);
  }
  .brand {
    display: flex; align-items: center; gap: 10px;
    font-weight: 700; color: var(--teal-bright);
    letter-spacing: .5px;
  }
  .brand-mark { width: 14px; height: 14px; background: var(--teal-bright); }

  /* services side */
  .card--services { display: flex; flex-direction: column; align-items: center; padding-top: 70px; }
  .card--services .brand { font-size: 34px; }
  .services-title {
    margin-top: 44px; font-size: 19px; font-weight: 500;
    color: var(--teal); text-transform: uppercase; letter-spacing: .3px;
  }
  .services-list { margin-top: 12px; text-align: center; font-size: 19px; line-height: 1.5; }
  .services-list .dot { color: var(--teal); padding: 0 4px; }

  /* contact side */
  .card--contact .brand { position: absolute; top: 58px; right: 36px; font-size: 26px; }
  .card--contact .rule-top {
    position: absolute; top: 122px; left: 36px; right: 36px;
    height: 1px; background: var(--rule);
  }
  .address {
    position: absolute; top: 138px; right: 36px;
    text-align: right; font-size: 15px; line-height: 1.4;
  }
  .abn { color: var(--teal); font-weight: 500; }
  .person { position: absolute; left: 36px; bottom: 28px; width: 250px; }
  .person-name { font-size: 26px; font-weight: 500; color: var(--teal); }
  .person-role { font-size: 15px; margin-top: 2px; }
  .person .rule { height: 1px; background: var(--rule); margin: 10px 0 10px; }
  .contact-list { list-style: none; font-size: 15px; line-height: 1.65; }
  .contact-list li { display: flex; align-items: center; gap: 10px; }
  .contact-list svg { width: 14px; height: 14px; flex: none; }
</style>
</head>
<body>
<main class="sheet">
  <section class="card card--services">
    <div class="brand"><span class="brand-mark"></span>Ridgeway Sparks</div>
    <h2 class="services-title">Services Offer</h2>
    <p class="services-list">
      <span class="dot">•</span>Breakdowns <span class="dot">•</span>Field Service <span class="dot">•</span>A/C Systems<br>
      <span class="dot">•</span>Machine rewires <span class="dot">•</span>Mine site vehicle fit outs
    </p>
  </section>

  <section class="card card--contact">
    <div class="brand"><span class="brand-mark"></span>Ridgeway Sparks</div>
    <div class="rule-top"></div>
    <address class="address" style="font-style:normal">
      421, Address line goes here<br>
      45452, Country name<br>
      <span class="abn">ABN No. 123-456</span>
    </address>
    <div class="person">
      <h1 class="person-name">Liam Carter</h1>
      <p class="person-role">Owner</p>
      <div class="rule"></div>
      <ul class="contact-list">
        <li>
          <svg viewBox="0 0 14 14" aria-hidden="true"><rect x="3.5" y="1" width="7" height="12" rx="1.2" fill="none" stroke="#00AB8E" stroke-width="1.3"/><line x1="6" y1="11" x2="8" y2="11" stroke="#00AB8E" stroke-width="1.2"/></svg>
          0412 558 301
        </li>
        <li>
          <svg viewBox="0 0 14 14" aria-hidden="true"><rect x="1" y="3" width="12" height="8.5" fill="#00AB8E"/><polyline points="1,3 7,8 13,3" fill="none" stroke="#000" stroke-width="1.2"/></svg>
          hello@ridgewaysparks.com
        </li>
        <li>
          <svg viewBox="0 0 14 14" aria-hidden="true"><circle cx="7" cy="7" r="5.8" fill="none" stroke="#00AB8E" stroke-width="1.3"/><ellipse cx="7" cy="7" rx="2.5" ry="5.8" fill="none" stroke="#00AB8E" stroke-width="1"/><line x1="1.2" y1="7" x2="12.8" y2="7" stroke="#00AB8E" stroke-width="1"/></svg>
          www.ridgewaysparks.com
        </li>
      </ul>
    </div>
  </section>
</main>
</body>
</html>
```